Trucking/service truck *Updated

Cards for a trucking company. Company transfers logs to saw mills. We are looking for something edgy, modern and fun. It's very limited when it comes to trucking business card choices. Plus the owner also runs an on-site service truck. He has 20+ years mechanic experience.
Colors are open. Favorites are orange & purple, but not must have. We really want to emphasize trust, dependability and knowledge with a bright, attention getter.
On card:
Halvorsen & Halvorsen
Dale Halvorsen - Owner/Manager/Maintenance 555-214-0937
Tami Halvorsen -Office Administration/Bookkeeping 555-630-4518
4170 Maple Rd.
Larkmoor, Oregon 97015
555-372-9061 - Office
Updates
Just a thought. Do you think you can combine the Taurus and Pisces signs? And put in the corner, or on the back or anything really? Thanks! You all or doing fantastic!

```html
<!DOCTYPE html>
<html lang="en">
<head>
<meta charset="utf-8">
<title>Halvorsen &amp; Halvorsen — Business Cards</title>
<link rel="stylesheet" href="https://fonts.googleapis.com/css2?family=Barlow:wght@400;500;700&display=swap">
<style>
  :root {
    --backdrop: #1d1e20;
    --card-face: #a2a5a8;
    --card-edge: #c3c6c9;
    --accent-blue: #1ea9dc;
    --ink-white: #f4f6f7;
    --ink-soft: #e3e6e8;
    --divider: #e9ecee;
  }
  * { box-sizing: border-box; margin: 0; padding: 0; }
  html, body {
    width: 1200px; height: 800px; overflow: hidden;
    background: var(--backdrop);
    font-family: "Barlow", "Helvetica Neue", Arial, sans-serif;
  }
  .stage {
    width: 1200px; height: 800px;
    display: flex; align-items: center; justify-content: center; gap: 40px;
  }
  .card {
    position: relative;
    width: 540px; height: 310px;
    border-radius: 22px;
    background: linear-gradient(160deg, #aeb1b4 0%, var(--card-face) 60%, #979a9d 100%);
    border: 1px solid var(--card-edge);
  }
  /* Front */
  .company-name {
    position: absolute; top: 42px; left: 0; right: 0;
    text-align: center;
    font-weight: 700; font-size: 31px; letter-spacing: 0.5px;
    color: var(--accent-blue); text-transform: uppercase;
  }
  .contact { position: absolute; }
  .contact--owner { left: 36px; top: 104px; }
  .contact--office { left: 300px; top: 168px; }
  .contact__name {
    font-weight: 700; font-size: 23px; color: var(--accent-blue); line-height: 1.05;
  }
  .contact__role {
    font-size: 12px; font-weight: 500; color: var(--ink-white); margin-top: 2px;
  }
  .contact__phone {
    font-size: 23px; font-weight: 400; color: var(--ink-soft);
    letter-spacing: 2px; margin-top: 4px;
  }
  .divider {
    position: absolute; left: 272px; top: 128px;
    width: 1.5px; height: 104px; background: var(--divider);
  }
  .office-line {
    position: absolute; left: 36px; right: 24px; bottom: 30px;
    font-size: 16px; font-weight: 500; color: var(--ink-white); letter-spacing: 1px;
    white-space: nowrap;
  }
  .office-line__label { font-weight: 700; margin-right: 8px; }
  .office-line__sep { margin: 0 12px; }
  /* Back */
  .card__frame { position: absolute; inset: 0; }
  .back-name {
    position: absolute; top: 50%; left: 0; right: 0; transform: translateY(-50%);
    text-align: center;
    font-weight: 700; font-size: 32px; letter-spacing: 0.5px;
    color: var(--ink-white); text-transform: uppercase;
  }
</style>
</head>
<body>
<main class="stage">
  <section class="card card--front" aria-label="Business card front">
    <h1 class="company-name">Halvorsen &amp; Halvorsen</h1>
    <div class="contact contact--owner">
      <p class="contact__name">Dale Halvorsen</p>
      <p class="contact__role">Owner/Manager/Maintenance</p>
      <p class="contact__phone">555 214 0937</p>
    </div>
    <div class="divider"></div>
    <div class="contact contact--office">
      <p class="contact__name">Tami Halvorsen</p>
      <p class="contact__role">Office Administration/Bookkeeping</p>
      <p class="contact__phone">555 630 4518</p>
    </div>
    <p class="office-line">
      <span class="office-line__label">O</span>555 - 372 - 9061<span class="office-line__sep">|</span>4170 Maple Rd., Larkmoor, Oregon 97015
    </p>
  </section>

  <section class="card card--back" aria-label="Business card back">
    <svg class="card__frame" width="540" height="310" viewBox="0 0 540 310">
      <rect x="24" y="22" width="492" height="266" rx="20" ry="20"
            fill="none" stroke="var(--accent-blue)" stroke-width="9"/>
    </svg>
    <h2 class="back-name">Halvorsen &amp; Halvorsen</h2>
  </section>
</main>
</body>
</html>
```